New Book Cover Design Project: Belly Balance and Calm Stomachs

5-1/2 x8-1/2 inch cover front and back, with spine for a 45,000-word book.
Title: Belly Balance and Calm Stomachs. Subtitle: Restore Your Inner Garden and Leave Behind Bloating Woes, Slow Energy, Mental Haze, Extra Pounds, and Swelling—for a Brighter, Lighter Self. Author: Mavis Thornquill. Thorough discussion of how to achieve good digestion and lifelong gut health mainly through a quality diet based on real food free of chemicals. Ten chapters. I am author of nine other books, focused on vibrant health through natural living. I'm looking for a simple and impactful cover. My most recent book, also with cover from Pixel Harbor, is The Lone Pantry Plan: Reshape Your Bond with Meals in Only 30 Days.

Target Market(s)

Mostly middle aged women who want to feel better and have real solutions for their digestion and gut problems, including less midriff fat

Industry/Entity Type

Self-help health information from a nutritionist and family health advocate.

Font styles to use
Serif

Colors

Designer to choose colors to be used in the design.

Requirements
Must have
• Some way to indicate the author is a woman, my name being Mavis Thornquill. Multicolored, upbeat, with some graphic reference to gut health but not with an illustration of microbes or intestinesnGra
Nice to have
• Perhaps an image of women's flat bellies or before and after images of flat bellies, or anything else suggestive of a smooth-functioning living systempas
Should not have
• See above.

```html
<!DOCTYPE html>
<html lang="en">
<head>
<meta charset="utf-8">
<title>Belly Balance and Calm Stomachs — Book Cover</title>
<link rel="stylesheet" href="https://fonts.googleapis.com/css2?family=Roboto:wght@400;900&family=Oswald:wght@500;600&family=Montserrat:wght@700;800&display=swap">
<style>
  :root {
    --paper: #ffffff;
    --blush: #f8d3e1;
    --plum: #a01f62;
    --fuchsia: #e9207a;
    --forest: #0f3a12;
    --ink: #2b2226;
    --white: #ffffff;
  }
  * { margin: 0; padding: 0; box-sizing: border-box; }
  html, body { width: 1200px; height: 887px; overflow: hidden; background: var(--paper); }
  .canvas { position: relative; width: 1200px; height: 887px; }
  .cover {
    position: absolute; left: 47px; top: 47px; width: 1107px; height: 794px;
    background: var(--blush); overflow: hidden;
  }
  .abs { position: absolute; }

  /* title lockup */
  .title { text-align: center; display: flex; flex-direction: column; align-items: center; }
  .title__top {
    font-family: "Roboto", Arial, sans-serif; font-weight: 900; color: var(--plum);
    line-height: 0.8; letter-spacing: -0.03em; white-space: nowrap;
  }
  .title__and {
    display: flex; align-items: center; width: 100%;
    font-family: "Roboto", Arial, sans-serif; font-weight: 900; color: var(--fuchsia);
    line-height: 1;
  }
  .title__and::before, .title__and::after { content: ""; flex: 1; height: 2px; background: var(--fuchsia); }
  .title__and span { padding: 0 0.3em; }
  .title__bottom {
    font-family: "Oswald", "Arial Narrow", sans-serif; font-weight: 600; color: var(--fuchsia);
    line-height: 1; white-space: nowrap; letter-spacing: 0.01em;
  }

  .title--front { left: 622px; top: 24px; width: 456px; }
  .title--front .title__top.l1 { font-size: 134px; }
  .title--front .title__top.l2 { font-size: 104px; margin-top: 12px; }
  .title--front .title__and { font-size: 36px; margin-top: 6px; }
  .title--front .title__bottom { font-size: 66px; margin-top: 4px; }

  .title--back { left: 31px; top: 66px; width: 217px; }
  .title--back .title__top.l1 { font-size: 64px; }
  .title--back .title__top.l2 { font-size: 50px; margin-top: 5px; }
  .title--back .title__and { font-size: 17px; margin-top: 3px; }
  .title--back .title__and::before, .title--back .title__and::after { height: 1px; }
  .title--back .title__bottom { font-size: 31px; margin-top: 2px; }

  /* back copy */
  .blurb {
    font-family: "Roboto", Arial, sans-serif; font-weight: 400; color: var(--ink);
    font-size: 16px; line-height: 18.1px;
  }
  .blurb--left { left: 31px; top: 238px; width: 230px; }
  .blurb--right { left: 291px; top: 68px; width: 194px; }
  .blurb--right p + p { margin-top: 22px; }

  /* images */
  .art-back { left: -10px; top: 522px; width: 340px; height: 340px; border-radius: 50%;
    background: radial-gradient(circle, #fbe7d6 0%, #e8b98e 35%, #c9583a 60%, #4f7a33 85%); }
  .portrait { left: 315px; top: 519px; width: 164px; height: 218px; border-radius: 40% 40% 10% 10%;
    background: linear-gradient(180deg, #4a2c22 0%, #7a4b3a 40%, #e8d6bd 75%, #f3e6d3 100%); opacity: 0.9; }
  .art-front { left: 716px; top: 361px; width: 268px; height: 268px; border-radius: 50%;
    background: radial-gradient(circle, #fff3e0 0%, #e9c79e 30%, #c7652f 58%, #4e7d34 80%, #7d2d4e 100%); }

  /* spine */
  .spine-title {
    left: 538px; top: 58px; height: 480px; writing-mode: vertical-rl;
    font-size: 26px; line-height: 1; white-space: nowrap;
  }
  .spine-title .a { font-family: "Roboto", Arial, sans-serif; font-weight: 900; color: var(--plum); }
  .spine-title .b { font-family: "Oswald", "Arial Narrow", sans-serif; font-weight: 600; color: var(--fuchsia); }
  .spine-author {
    left: 543px; top: 548px; writing-mode: vertical-rl;
    font-family: "Montserrat", Arial, sans-serif; font-weight: 700; font-size: 13.5px;
    letter-spacing: 0.14em; color: var(--ink); white-space: nowrap; line-height: 1;
  }

  /* subtitle */
  .subtitle {
    left: 628px; top: 643px; width: 446px; text-align: center;
    font-family: "Montserrat", Arial, sans-serif; font-weight: 700; font-size: 15.5px;
    line-height: 25px; color: var(--forest);
  }
  .subtitle em { font-style: normal; color: var(--fuchsia); }

  /* band */
  .band {
    left: 0; top: 760px; width: 1107px; height: 34px;
    background: linear-gradient(90deg, var(--plum) 0%, var(--fuchsia) 28%, var(--plum) 50%, var(--fuchsia) 72%, var(--plum) 100%);
  }
  .band__author {
    position: absolute; left: 700px; width: 260px; top: 0; height: 34px; line-height: 34px; text-align: center;
    font-family: "Montserrat", Arial, sans-serif; font-weight: 800; font-size: 16px;
    letter-spacing: 0.2em; color: var(--white); white-space: nowrap;
  }
</style>
</head>
<body>
<div class="canvas">
  <div class="cover">
    <!-- back cover -->
    <div class="abs title title--back">
      <div class="title__top l1">BELLY</div>
      <div class="title__top l2">BALANCE</div>
      <div class="title__and"><span>AND</span></div>
      <div class="title__bottom">CALM STOMACHS</div>
    </div>

    <div class="abs blurb blurb--left">
      <p>Lorem ipsum dolor sit amet, consectetur adipiscing elit, sed do eiusmod tempor incididunt ut labore et dolore magna aliqua. Quis ipsum suspendisse ultrices gravida. Risus commodo viverra maecenas accumsan lacus vel facilisis. do eiusmod tempor incididunt ut labore et dolore magna aliqua. Quis ipsum suspendisse ultrices gravida. Risus commodo viverra maecenas accumsan lacus vel</p>
    </div>

    <div class="abs blurb blurb--right">
      <p>Lorem ipsum dolor sit amet, consectetur adipiscing elit, sed do eiusmod tempor incididunt ut labore et dolore magna aliqua. Quis ipsum suspendisse ultrices gravida. Risus commodo viverra maecenas accumsan lacus vel facilisis.commodo viverra</p>
      <p>Lorem ipsum dolor sit amet, consectetur adipiscing elit, sed do eiusmod t empor incididunt ut labore et dolore magna aliqua. Quis ipsum suspendisse ultrices gravida. Risus commodo viverra maecenas accumsan</p>
    </div>

    <div class="abs art-back" role="img" aria-label="Ring of colourful whole foods — vegetables, berries, seeds and nuts — spiralling around a glowing centre"></div>
    <div class="abs portrait" role="img" aria-label="Portrait photograph of the author, Mavis Thornquill"></div>

    <!-- spine -->
    <div class="abs spine-title"><span class="a">BELLY BALANCE </span><span class="b">AND CALM STOMACHS</span></div>
    <div class="abs spine-author">MAVIS THORNQUILL</div>

    <!-- front cover -->
    <div class="abs title title--front">
      <div class="title__top l1">BELLY</div>
      <div class="title__top l2">BALANCE</div>
      <div class="title__and"><span>AND</span></div>
      <div class="title__bottom">CALM STOMACHS</div>
    </div>

    <div class="abs art-front" role="img" aria-label="Circular arrangement of colourful whole foods — cucumbers, berries, greens, seeds, nuts and grains — spiralling toward a glowing centre"></div>

    <p class="abs subtitle">Restore Your <em>Inner Garden</em> and Leave Behind <em>Bloating Woes, Slow Energy, Mental Haze, Extra Pounds,</em> and <em>Swelling</em> —for a Brighter, Lighter Self</p>

    <div class="abs band"><span class="band__author">MAVIS THORNQUILL</span></div>
  </div>
</div>
</body>
</html>
```